Kiswa Design

We need a flyer design for a product that we are a selling, a sacred Islamic cloth called a Kiswah, which is draped around the holy Kaaba in mecca every year.

The details we would like on the flyer are as follows:

Rare Kiswah of the holy Kaaba for sale (fitted in 1977 and 1982 vintage). For sale:

1) whole piece 15 meters x 2.60 meters : £60,000
2) 8 meters x 2.60 meters : £31,200
3) 4 meters x 2.60 meters : £15,600
4) 1 meter : £1500

(insert a high quality picture of holy Kaaba here, then underneath the picture, write the following:) "The Kaaba is covered by an expensive black cloth which is known as 'Kiswah' which is produced and changed every year"

(insert picture of our product here,i.e. use the document named MAIN IMAGE then underneath this picture write the following:) "Silk lampas weave Kiswah, woven silk on a black satin ground with Quranic calligraphy, the zig-zag bands of inscription alternate with the Shahadah and the inscription, 'God, exalted be His Glory!"

insert another picture of kiswah which i provided anywhere you like

(somewhere on flyer write the following) please note a percentage of sales will go towards Sadaqah for our Muslim brothers and sisters in need around the world

(somewhere on flyer write the following) Hallorand's international auction house authenticity document also available to prove the Kiswah is genuine.

100% genuine

contact us today! deals this good don't last forever.

email: relicoffer@tarnwickmail.com

Please use the images that I have attached on the flyer accordingly. Also feel free to be as creative as possible I want it to attract a lot of attention but also look professional so you may add some things to improve the look of the flyer.

note: the product being sold is on the pictures I've provided, in particular, i want file 2 "main image" in a large size on the flyer!

thank you! and happy holidays

Muslims and Islamic collectors

House

• the dimensions of the flyer is :
• A5 horizontal or vertical
• (210 x 148 mm)
• must have colors! up to you what colors to choose!

```html
<!DOCTYPE html>
<html lang="en">
<head>
<meta charset="utf-8">
<title>Rare Kiswah of the Holy Kaaba for Sale</title>
<link rel="stylesheet" href="https://fonts.googleapis.com/css2?family=Anton&family=Oswald:wght@400;500;600;700&display=swap">
<style>
  :root {
    --green: #11934a;
    --green-dark: #0c7a3b;
    --sage: #b8d2b4;
    --sage-light: #c9dfc5;
    --ink: #141414;
    --white: #ffffff;
    --cloth-dark: #1c2022;
    --cloth-mid: #4a5052;
  }
  * { margin: 0; padding: 0; box-sizing: border-box; }
  html, body { width: 923px; height: 1200px; overflow: hidden; }
  body {
    position: relative;
    background: radial-gradient(ellipse at 50% 45%, var(--sage-light), var(--sage) 75%);
    font-family: "Oswald", "Arial Narrow", sans-serif;
    color: var(--ink);
    text-transform: uppercase;
  }
  .title-band {
    position: absolute; left: 25px; top: 20px; width: 873px; height: 86px;
    background: var(--green);
    clip-path: polygon(0 12%, 4% 0, 96% 0, 100% 12%, 100% 88%, 96% 100%, 4% 100%, 0 88%);
    display: flex; align-items: center; justify-content: center;
    border-top: 3px solid var(--white); border-bottom: 3px solid var(--white);
  }
  .title-band h1 {
    font-family: "Anton", "Impact", sans-serif; font-weight: 400;
    color: var(--white); font-size: 38px; line-height: 1.05; text-align: center; letter-spacing: 0.5px;
  }
  .sale-tag {
    position: absolute; left: 110px; top: 150px; width: 46px; height: 172px;
    background: var(--green); border: 3px solid var(--white);
    display: flex; align-items: center; justify-content: center;
  }
  .sale-tag span {
    transform: rotate(-90deg); white-space: nowrap;
    font-family: "Anton", sans-serif; color: var(--white); font-size: 30px; letter-spacing: 1px;
  }
  .price-list { position: absolute; left: 172px; top: 150px; list-style: none; }
  .price-list li { font-size: 29px; font-weight: 500; line-height: 42px; letter-spacing: 0.3px; }
  .photo {
    position: absolute; border: 4px solid var(--white);
  }
  .kaaba-photo {
    left: 660px; top: 270px; width: 134px; height: 130px;
    background: linear-gradient(180deg, #8fb4dc 0 38%, #1d1d1d 38% 78%, #e9e9e6 78%);
  }
  .cloth-circle {
    position: absolute; width: 272px; height: 272px; border-radius: 50%;
    border: 6px solid var(--white);
    background: radial-gradient(circle at 45% 40%, var(--cloth-mid), var(--cloth-dark) 75%);
    z-index: 2;
  }
  .circle-one { left: 50px; top: 328px; }
  .circle-two { left: 595px; top: 620px; background: radial-gradient(circle at 50% 40%, #7a8082, #2c3133 80%); }
  .quote-box {
    position: absolute; background: var(--green); border: 3px solid var(--white);
    color: var(--white); font-size: 24px; font-weight: 500; line-height: 1.2; letter-spacing: 0.6px;
    text-align: center; display: flex; align-items: center;
  }
  .quote-kaaba { left: 300px; top: 394px; width: 610px; height: 172px; border-radius: 0 26px 26px 0; padding: 0 40px 0 90px; }
  .quote-cloth { left: 42px; top: 648px; width: 590px; height: 212px; border-radius: 26px 0 0 26px; padding: 0 110px 0 30px; }
  .folded-photo {
    left: 59px; top: 913px; width: 166px; height: 164px;
    background: linear-gradient(160deg, #6c7072, #2a2e30 55%, #505456);
  }
  .notes { position: absolute; left: 246px; top: 926px; width: 660px; }
  .notes p { font-size: 19px; font-weight: 500; line-height: 38px; letter-spacing: 0.3px; }
  .notes p + p { margin-top: 2px; }
  .contact-band {
    position: absolute; left: 25px; top: 1078px; width: 873px; height: 104px;
    background: var(--green);
    clip-path: polygon(0 12%, 4% 0, 96% 0, 100% 12%, 100% 88%, 96% 100%, 4% 100%, 0 88%);
    border-top: 3px solid var(--white);
    color: var(--white);
  }
  .genuine {
    position: absolute; left: 50px; top: 8px; width: 160px; text-align: center;
    font-family: "Anton", sans-serif; font-size: 40px; line-height: 1;
  }
  .divider { position: absolute; left: 220px; top: 14px; width: 3px; height: 80px; background: var(--white); }
  .cta { position: absolute; left: 245px; top: 12px; font-size: 30px; font-weight: 600; }
  .cta small { font-size: 20px; font-weight: 500; }
  .email { position: absolute; left: 245px; top: 60px; font-size: 21px; letter-spacing: 7px; font-weight: 500; }
</style>
</head>
<body>
  <header class="title-band">
    <h1>Rare Kiswah of the Holy Kaaba for Sale<br>(Fitted in 1977 and 1982 Vintage).</h1>
  </header>

  <div class="sale-tag"><span>For Sale</span></div>
  <ol class="price-list">
    <li>1) Whole piece 15 meters x 2.60 meters : £60,000</li>
    <li>2) 8 meters x 2.60 meters : £31,200</li>
    <li>3) 4 meters x 2.60 meters : £15,600</li>
    <li>4) 1 meter : £1500</li>
  </ol>

  <div class="photo kaaba-photo" role="img" aria-label="Photograph of the Kaaba draped in its black Kiswah in Mecca"></div>

  <div class="cloth-circle circle-one" role="img" aria-label="Close-up of black Kiswah cloth with woven calligraphy"></div>
  <p class="quote-box quote-kaaba">"The Kaaba is covered by an expensive black cloth which is known as 'Kiswah' which is produced and changed every year"</p>

  <p class="quote-box quote-cloth">"Silk lampas weave Kiswah, woven silk on a black satin ground with Quranic calligraphy, the zig-zag bands of inscription alternate with the Shahadah and the inscription, 'God, exalted be His Glory!"</p>
  <div class="cloth-circle circle-two" role="img" aria-label="Kiswah silk showing zig-zag bands of Quranic inscription"></div>

  <div class="photo folded-photo" role="img" aria-label="Folded length of black Kiswah cloth"></div>
  <div class="notes">
    <p>Please note a percentage of sales will go towards Sadaqah<br>for our Muslim brothers and sisters in need around the world</p>
    <p>Hallorand's international auction house authenticity<br>document also available to prove the Kiswah is genuine.</p>
  </div>

  <footer class="contact-band">
    <div class="genuine">100%<br>Genuine</div>
    <div class="divider"></div>
    <p class="cta">Contact us today! <small>Deals this good don't last forever.</small></p>
    <p class="email">Email: relicoffer@tarnwickmail.com</p>
  </footer>
</body>
</html>
```